Webpages for Tuomivaara Software Consulting

Needed: Webpage design.
Details:
One page site with good looking fonts and simple modern design. Logo would also be nice.
Page is for Software consulting company called: "Tuomivaara Software Consulting". Tuomivaara is my surname.
Pages should tell viewer that the company is reliable and its employees are hard-core professionals.
Company currently has one employee, that's me. So what I do is what this company does. I am software consultant. Basicly that means that I do Java/JavaEE/Web programming as subcontractor.
Here is more detail information about me.
SPECIALTIES
- Enterprise J2EE Application Programming and Architectures,
- Web development and
- Agile development.
I have over a decade of experience on designing and creating Java based web-services and applications to multiple interfaces. I also have plenty of experience about software architectures, design patterns and integration into third party systems. I’ve got good knowledge about agile software development and testing processes and I am experienced ScrumMaster and software project leader.
Target Market(s)
IT Businesses, Coding companies... Anyone who is buying coding as service.
Industry/Entity Type
Software
Look and feel

```html
<!DOCTYPE html>
<html lang="en">
<head>
<meta charset="utf-8">
<title>Tuomivaara Software Consulting — How We Work</title>
<link href="https://fonts.googleapis.com/css2?family=Fira+Sans+Extra+Condensed:wght@500;700&family=Open+Sans:wght@300&display=swap" rel="stylesheet">
<style>
  :root {
    --ink: #2b2b2b;
    --heading-grey: #c6c6c6;
    --rule-grey: #dcdcdc;
    --piece-grey: #cfcfcf;
    --step-blue: #0e9fd3;
    --step-rim: #0a8bbf;
    --step-shade: rgba(0, 70, 110, 0.35);
    --white: #ffffff;
  }
  * { margin: 0; padding: 0; box-sizing: border-box; }
  html, body {
    width: 1200px;
    height: 904px;
    overflow: hidden;
    background: var(--white);
  }
  .page {
    position: relative;
    width: 1200px;
    height: 904px;
  }

  /* Brand */
  .brand {
    position: absolute;
    left: 102px;
    top: 100px;
    display: flex;
    align-items: center;
    gap: 16px;
    color: var(--ink);
    font-family: "Fira Sans Extra Condensed", sans-serif;
    font-weight: 500;
    text-transform: uppercase;
  }
  .brand-mark {
    width: 60px;
    height: 60px;
    background: var(--ink);
  }
  .brand-name {
    font-size: 34px;
    line-height: 30px;
    letter-spacing: 0.5px;
  }
  .brand-name small {
    display: block;
    font-size: 20px;
    line-height: 22px;
    letter-spacing: 0.3px;
  }

  /* Navigation */
  .main-nav {
    position: absolute;
    top: 116px;
    right: 97px;
    display: flex;
    gap: 0;
  }
  .main-nav a {
    font-family: "Fira Sans Extra Condensed", sans-serif;
    font-weight: 500;
    font-size: 20px;
    color: var(--ink);
    text-decoration: none;
    text-transform: uppercase;
    margin-left: 55px;
  }

  /* Section heading */
  .section-title {
    position: absolute;
    left: 100px;
    top: 276px;
    font-family: "Fira Sans Extra Condensed", sans-serif;
    font-weight: 700;
    font-size: 70px;
    line-height: 70px;
    letter-spacing: -2px;
    color: var(--heading-grey);
    text-transform: uppercase;
  }
  .section-rule {
    position: absolute;
    left: 97px;
    top: 338px;
    width: 912px;
    height: 1px;
    background: var(--rule-grey);
  }
  .section-emblem {
    position: absolute;
    left: 984px;
    top: 256px;
    width: 118px;
    height: 148px;
    border-radius: 18px;
    background: var(--piece-grey);
  }

  /* Process steps */
  .process {
    position: absolute;
    left: 88px;
    top: 508px;
    display: flex;
    gap: 14px;
    list-style: none;
  }
  .step {
    width: 248px;
    height: 248px;
    border-radius: 50%;
    background: var(--step-blue);
    border: 7px solid var(--step-rim);
    display: flex;
    flex-direction: column;
    align-items: center;
    padding-top: 70px;
    color: var(--white);
  }
  .step-icon {
    width: 34px;
    height: 34px;
  }
  .step-shadow {
    width: 26px;
    height: 4px;
    border-radius: 50%;
    background: var(--step-shade);
    margin-top: 1px;
  }
  .step-label {
    font-family: "Open Sans", sans-serif;
    font-weight: 300;
    font-size: 29px;
    line-height: 34px;
    margin-top: 9px;
    letter-spacing: -0.3px;
    text-transform: uppercase;
  }
</style>
</head>
<body>
<div class="page">

  <header>
    <div class="brand">
      <span class="brand-mark"></span>
      <div class="brand-name">Tuomivaara<small>Software Consulting</small></div>
    </div>
    <nav class="main-nav">
      <a href="#how">How we work</a>
      <a href="#who">Who we are</a>
      <a href="#what">What we do</a>
      <a href="#contact">Contact us</a>
    </nav>
  </header>

  <section id="how">
    <h1 class="section-title">How we work</h1>
    <div class="section-rule"></div>
    <div class="section-emblem" role="img" aria-label="Grey jigsaw puzzle piece decoration"></div>

    <ol class="process">
      <li class="step">
        <svg class="step-icon" viewBox="0 0 34 34" aria-hidden="true">
          <circle cx="13" cy="13" r="7" fill="none" stroke="#fff" stroke-width="3.5"/>
          <line x1="18" y1="18" x2="28" y2="26" stroke="#fff" stroke-width="5" stroke-linecap="round"/>
        </svg>
        <span class="step-shadow"></span>
        <span class="step-label">Analyze</span>
      </li>
      <li class="step">
        <svg class="step-icon" viewBox="0 0 34 34" aria-hidden="true">
          <polygon points="6,5 10,3 27,24 28,31 22,27" fill="#fff"/>
        </svg>
        <span class="step-shadow"></span>
        <span class="step-label">Design</span>
      </li>
      <li class="step">
        <svg class="step-icon" viewBox="0 0 34 34" aria-hidden="true">
          <path d="M12 3 A7 7 0 0 0 6 13 L9 10 L13 11 L14 15 L11 18 A7 7 0 0 0 16 14 L27 27 L30 24 L18 12 A7 7 0 0 0 12 3 Z" fill="#fff"/>
          <rect x="23" y="22" width="6" height="7" rx="1" transform="rotate(-45 26 25)" fill="#fff"/>
        </svg>
        <span class="step-shadow"></span>
        <span class="step-label">Development</span>
      </li>
      <li class="step">
        <svg class="step-icon" viewBox="0 0 34 34" aria-hidden="true">
          <polygon points="4,17 9,13 14,19 27,4 31,8 14,29" fill="#fff"/>
        </svg>
        <span class="step-shadow"></span>
        <span class="step-label">Implement</span>
      </li>
    </ol>
  </section>

</div>
</body>
</html>
```